Business Cards for Logistics Company

Looking to update Business Card Design.
Logo is attached. Blue background is not a part of the logo, you can remove it in layers.

Company: Harbor Crest Freightways
Industry: Logistics, Container Shipping

Address:
418 Willow Bend Ave
Bayonne NJ 07419

Phones:
p. 201-555-0143
f. 201-555-0178
c. very by person's name

Website: www.hcfroute.example

Design has to include person's name and position.
OLD Design is included.

B2B

Business

Card Size (non standard): 1039 x 697 pixels, 300dpi
Template is attached.

Font styles to use
Serif
Sans Serif

```html
<!DOCTYPE html>
<html lang="en">
<head>
<meta charset="utf-8">
<title>Harbor Crest Freightways – Business Card</title>
<link rel="stylesheet" href="https://fonts.googleapis.com/css2?family=PT+Sans:wght@400;700&family=Share+Tech+Mono&display=swap">
<style>
  :root {
    --stage: #000000;
    --paper: #ffffff;
    --ink: #1d1d1f;
    --brand-blue: #1f7cc6;
    --brand-square: #2a63b8;
    --band-top: #1a2757;
    --band-bottom: #2a3d7c;
    --band-text: #ffffff;
  }
  * { box-sizing: border-box; margin: 0; padding: 0; }
  html, body { width: 1200px; height: 900px; overflow: hidden; background: var(--stage); }
  .stage { position: relative; width: 1200px; height: 900px; }

  .card {
    position: absolute; top: 275px; width: 477px; height: 294px;
    background: var(--paper); overflow: hidden;
    font-family: "PT Sans", Arial, sans-serif; color: var(--ink);
  }
  .card--front { left: 116px; border-radius: 0 62px 0 62px; }
  .card--back  { left: 622px; border-radius: 62px 0 62px 0; }

  .brand-mark { position: absolute; background: var(--brand-square); }
  .card--front .brand-mark { left: 92px; top: 50px; width: 100px; height: 100px; }
  .card--back  .brand-mark { left: 108px; top: 50px; width: 92px; height: 92px; }

  .brand-name {
    position: absolute; font-family: "Share Tech Mono", "Courier New", monospace;
    font-size: 17px; line-height: 20px; letter-spacing: 2.2px; color: var(--ink);
    text-transform: uppercase;
  }
  .brand-name span { display: block; }
  .brand-name span + span { font-size: 14px; letter-spacing: 3.4px; }
  .card--front .brand-name { left: 209px; top: 74px; }
  .card--back  .brand-name { left: 212px; top: 71px; }

  .holder { position: absolute; right: 237px; top: 183px; text-align: right; }
  .holder__name { font-size: 17px; font-weight: 700; color: var(--brand-blue); line-height: 20px; }
  .holder__role { font-size: 14px; line-height: 18px; margin-top: 2px; }

  .contacts { position: absolute; left: 274px; top: 183px; list-style: none; font-size: 13.5px; }
  .contacts li { display: flex; align-items: center; height: 20px; }
  .contacts svg { width: 11px; height: 11px; margin-right: 8px; fill: var(--brand-blue); }

  .band {
    position: absolute; left: 0; right: 0; bottom: 0; height: 61px;
    background: linear-gradient(var(--band-top), var(--band-bottom));
    color: var(--band-text); display: flex; align-items: center; justify-content: center;
    font-size: 14px; padding-bottom: 4px;
  }
  .band--web { font-weight: 700; }

  .tagline {
    position: absolute; right: 267px; top: 159px; text-align: right;
    font-size: 15.5px; font-weight: 700; color: var(--brand-blue); line-height: 20px;
  }
  .services { position: absolute; left: 230px; top: 159px; list-style: none; font-size: 14px; line-height: 20px; }
  .services li { display: flex; align-items: center; }
  .services li::before {
    content: ""; width: 8px; height: 8px; border-radius: 50%;
    background: var(--brand-blue); margin-right: 10px;
  }
</style>
</head>
<body>
<main class="stage">
  <section class="card card--front">
    <div class="brand-mark"></div>
    <div class="brand-name"><span>Harbor Crest</span><span>Freightways</span></div>
    <div class="holder">
      <p class="holder__name">Viktor Lensky</p>
      <p class="holder__role">General Manager</p>
    </div>
    <ul class="contacts">
      <li><svg viewBox="0 0 24 24" aria-hidden="true"><path d="M6.6 10.8a15.1 15.1 0 0 0 6.6 6.6l2.2-2.2a1 1 0 0 1 1-.25 11.4 11.4 0 0 0 3.6.57 1 1 0 0 1 1 1V20a1 1 0 0 1-1 1A17 17 0 0 1 3 4a1 1 0 0 1 1-1h3.5a1 1 0 0 1 1 1c0 1.25.2 2.45.57 3.57a1 1 0 0 1-.25 1z"/></svg>201-555-0143</li>
      <li><svg viewBox="0 0 24 24" aria-hidden="true"><path d="M6 2h9l3 3v4H6zM3 10h18v11H3zm4 3v2h3v-2zm5 0v2h5v-2zm-5 4v2h3v-2z"/></svg>201-555-0178</li>
    </ul>
    <div class="band">418 Willow Bend Ave Bayonne NJ 07419</div>
  </section>

  <section class="card card--back">
    <div class="brand-mark"></div>
    <div class="brand-name"><span>Harbor Crest</span><span>Freightways</span></div>
    <p class="tagline">International<br>Transportation<br>Solutions</p>
    <ul class="services">
      <li>Ocean &amp; Air Freight</li>
      <li>Loading &amp; Storage</li>
      <li>Multimodal Transport</li>
    </ul>
    <div class="band band--web">www.hcfroute.example</div>
  </section>
</main>
</body>
</html>
```